'Recalibrating Columbia' is a political thriller novel

I need a book cover for a political thriller. The book is about a presidential campaign in 2024. A politician has a revolutionary new idea on how to move the economy from growing on debt based to thriving in abundance. A billionaire oil (Brandt) family undermines his campaign with blistering negative adds. A technology billionaire attempts to assassinate him. But ultimately the incumbent president seeking a third term will not give up power...
There is an underlying theory of economics told that is meant to educate the reader about how the majority of Americans and people around the world are trying to get by in a rigged system. Although the majority of people are much worse of then they need to be the truth is nobody is winning with the current economy (unless there sinister motivations involved). The story makes dire predictions of a technological dystopia.
Updates
Author's name: Tomas Ridley
Reason: There are so many very good choices but I haven't found the perfect one yer.
Target Market(s)
Anyone who is interested in living in a better world and changing what is not working and clearly getting worse.
Industry/Entity Type
Political
Colors
Designer to choose colors to be used in the design.
Look and feel
Each slider illustrates characteristics of the customer's brand and the style your logo design should communicate.

```html
<!DOCTYPE html>
<html lang="en">
<head>
<meta charset="utf-8">
<title>Recalibrating Columbia — Cover</title>
<link rel="stylesheet" href="https://fonts.googleapis.com/css2?family=Saira+Extra+Condensed:wght@500&family=Questrial&family=Oswald:wght@500&display=swap">
<style>
  :root {
    --ink-black: #0d0d0d;
    --stripe-grey: #3a3a3a;
    --flag-red: #b3221c;
    --flag-cream: #e6dcae;
    --title-yellow: #ffd400;
    --author-white: #ffffff;
  }
  html, body {
    margin: 0;
    padding: 0;
    width: 849px;
    height: 1200px;
    overflow: hidden;
    background: var(--ink-black);
  }
  .cover {
    display: block;
    width: 849px;
    height: 1200px;
  }
  .author-name {
    font-family: "Questrial", "Century Gothic", sans-serif;
    font-size: 50px;
    fill: var(--author-white);
    letter-spacing: 1px;
  }
  .title-line {
    font-family: "Saira Extra Condensed", "Agency FB", sans-serif;
    font-weight: 500;
    fill: var(--title-yellow);
    opacity: 0.93;
  }
  .dollar-glyph {
    font-family: "Oswald", sans-serif;
    font-weight: 500;
    fill: var(--flag-red);
    opacity: 0.9;
  }
</style>
</head>
<body>
<svg class="cover" viewBox="0 0 849 1200" xmlns="http://www.w3.org/2000/svg">
  <defs>
    <linearGradient id="backdrop-tone" x1="0" y1="0" x2="1" y2="1">
      <stop offset="0" stop-color="#2b2b2b"/>
      <stop offset="0.5" stop-color="#1a1a1a"/>
      <stop offset="1" stop-color="#262626"/>
    </linearGradient>
  </defs>

  <g class="backdrop" role="img" aria-label="Weathered black-and-white painted flag filling the cover, with a large dollar sign painted in red, cream and blue flag colours at its centre">
    <rect width="849" height="1200" fill="url(#backdrop-tone)"/>
    <text class="dollar-glyph" x="426" y="1040" font-size="1120" text-anchor="middle" aria-hidden="true">$</text>
  </g>

  <text class="author-name" x="424" y="64" text-anchor="middle">AUTHOR NAME</text>

  <g class="book-title">
    <text class="title-line" x="424" y="605" font-size="215" text-anchor="middle" textLength="776" lengthAdjust="spacingAndGlyphs">RECALIBRATING</text>
    <text class="title-line" x="424" y="852" font-size="215" text-anchor="middle" textLength="776" lengthAdjust="spacingAndGlyphs">COLUMBIA</text>
  </g>
</svg>
</body>
</html>
```